Redesign of outdated "Automotive Automation Company"

We are looking to finally update our outdated website with some cutting edge graphics. We want our customers to know we value technology and are cutting edge as far as design. We provide automation solutions for the automotive industry which essentially means we program robots, and sell automation related products.

Current URL

http://lnk.vemrota.com/Qx7pwe
Updates

Project Deadline Extended
Reason: The client portal wasn't working, it's just finally been fixed by Pixel Harbor. I will go through and start reviewing designs.

We are trying to go with the same look and feel on our business cards, line cards, apparel, etc. so we are forming a brand. I have included the current draft of the line card. Please utilize our newest Logo TLV Standardized Logo.jpg http://img.solvarenpics.com/pz3Tm8d.jpg?1 Also we are trying hard to sell the following software / hardware companies so we can put some emphasis on their product. Meridel Controls https://www.meridelcontrols.com/ We make money on selling the software and then on the integration. I think you should tie in this animation. ยท From Shop Chaos to Smooth Output https://media.vorplexclips.com/deliveries/938127a4b51dfe03c7724bde1209f74a615b830c.jpg?image_play_button=true&image_play_button_color=7b796ae0&image_crop_resized=275x155 In this 2-minute video, discover how Quellwave can help run your plant floor. We are Authorized Integrators / Resellers for Tamberly Mechatronics Varnoth Sensorik http://varnoth.com/en/usa/ Meridel Controls https://www.meridelcontrols.com/ Corvane Process Works www.cpwkx.com Halberd Transfer Corp www.halberdtransfer.com Pennwick Machining http://www.pennwickmachining.com/strategic_partners.aspx

Target Market(s)

Large automotive companies looking for automation or robotic programming. So Professional is key.

Industry/Entity Type

Automotive

Font styles to use
Other font styles liked:
• Possible Open Sans or Lato

Colors
0591cc
ceeaf6
fbd4d5
fbf289
fece3e

Requirements
Must have
• Professional Modern Design.

I want a homepage design, and a rough Sales Page... Where numerous products can be listed.
Nice to have
• Maybe an updated logo if possible.

```html
<!DOCTYPE html>
<html lang="en">
<head>
<meta charset="utf-8">
<title>TLV Engineering Solutions</title>
<link href="https://fonts.googleapis.com/css2?family=Lato:wght@400;700&family=Open+Sans:wght@400;600&display=swap" rel="stylesheet">
<style>
:root{
  --blue:#0591cc;--blue-lt:#1fb0e2;--red:#d61a4b;--red-lt:#ef3663;
  --olive:#b8b716;--olive-lt:#d6d530;--green:#4f9a24;--green-lt:#74b83b;
  --gold:#e3cf0d;--ink:#333;--muted:#555;--page:#ebebeb;--footer:#2b2b2b;
}
*{box-sizing:border-box;margin:0;padding:0}
html,body{width:920px;height:1200px;overflow:hidden}
body{position:relative;background:var(--page);font-family:"Open Sans",sans-serif;color:var(--ink)}
.header{position:absolute;left:0;top:0;width:920px;height:113px;background:linear-gradient(#f2f2f2,#e4e4e4)}
.brand{position:absolute;left:46px;top:26px;display:flex;align-items:center;gap:12px}
.brand-mark{width:56px;height:56px;border-radius:50%;background:var(--blue)}
.brand-name{font-family:"Lato",sans-serif;font-weight:700;font-size:19px;line-height:21px;color:#222;letter-spacing:1px}
.phone{position:absolute;left:491px;top:71px;font-family:"Lato",sans-serif;font-weight:700;font-size:13px;color:#222}
.payments{position:absolute;left:661px;top:36px;width:213px;height:48px;border:1px solid #c9c9c9;border-radius:3px;background:#f7f7f7}
.payments .label{position:absolute;left:14px;top:-8px;background:#eee;padding:0 3px;font-family:"Open Sans",sans-serif;font-size:10px;color:var(--muted)}
.cards{position:absolute;left:8px;top:12px;display:flex;gap:6px}
.cards span{width:45px;height:28px;border:1px solid #ccc;background:#fff;font-family:"Open Sans",sans-serif;font-size:8px;color:var(--muted);display:flex;align-items:center;justify-content:center}
.nav{position:absolute;left:0;top:113px;width:920px;height:38px;background:linear-gradient(#2fb7e4,#0a8fc6);display:flex;align-items:center;padding-left:45px}
.nav a{color:#fff;text-decoration:none;font-size:11.5px}
.nav .sep{color:#fff;margin:0 19px;font-size:11px}
.hero{position:absolute;left:0;top:151px;width:920px;height:265px;background:linear-gradient(135deg,#8a8f95 0%,#b9bcbf 40%,#6f7479 70%,#a5a8ab 100%)}
.hero-title{position:absolute;left:44px;top:65px;font-family:"Lato",sans-serif;font-size:21px;color:#fff}
.hero-text{position:absolute;left:45px;top:100px;width:210px;font-size:8.5px;line-height:12px;color:#fff}
.hero-btn{position:absolute;left:48px;top:144px;width:79px;height:30px;border-radius:3px;background:linear-gradient(#f2e12a,#d1bb00);font-family:"Lato",sans-serif;font-weight:700;font-size:9.5px;color:#4a4200;display:flex;align-items:center;justify-content:center}
.dots{position:absolute;left:433px;top:230px;display:flex;gap:11px}
.dots i{width:10px;height:10px;border-radius:50%;background:#b7bcc2}
.dots i.on{background:var(--gold)}
.welcome{position:absolute;left:0;top:416px;width:920px;height:187px;background:#fff;text-align:center}
.welcome h1{margin-top:32px;font-family:"Lato",sans-serif;font-weight:700;font-size:21px;color:#333}
.welcome p{margin:14px auto 0;width:820px;font-size:9.8px;line-height:17px;color:#444}
.btn{display:inline-flex;align-items:center;justify-content:center;border-radius:3px;color:#fff;font-family:"Lato",sans-serif;font-weight:700;font-size:9.5px}
.welcome .btn{margin-top:10px;width:75px;height:27px;background:linear-gradient(#26a9d8,#0b7fb2)}
.shade{position:absolute;left:130px;width:660px;height:14px;border-radius:50%;background:radial-gradient(ellipse at center,rgba(0,0,0,.25),rgba(0,0,0,0) 70%)}
.panels{position:absolute;left:46px;top:634px;display:flex;gap:10px}
.panel{width:201px;height:448px;background:linear-gradient(#fff,#eeeeee)}
.panel-head{height:49px;padding:16px 13px;font-family:"Lato",sans-serif;font-weight:700;font-size:13px;color:#fff;white-space:nowrap;letter-spacing:-.2px}
.panel-photo{margin:10px 10px 0;height:121px}
.panel-text{margin:18px 11px 0;font-size:8.8px;line-height:17px;color:#444;hyphens:auto}
.panel ul{list-style:none;margin:9px 11px 0}
.panel li{position:relative;padding-left:14px;font-size:9.6px;line-height:17px}
.panel li::before{content:"";position:absolute;left:0;top:5px;border-left:4px solid currentColor;border-top:3.5px solid transparent;border-bottom:3.5px solid transparent}
.panel .btn{margin:11px 10px 0;width:60px;height:24px;font-weight:400;font-size:9px}
.red .panel-head,.red .btn{background:linear-gradient(var(--red-lt),var(--red))}
.red li{color:var(--red)}
.olive .panel-head,.olive .btn{background:linear-gradient(var(--olive-lt),var(--olive))}
.olive li{color:var(--olive)}
.green .panel-head,.green .btn{background:linear-gradient(var(--green-lt),var(--green))}
.green li{color:var(--green)}
.blue .panel-head,.blue .btn{background:linear-gradient(var(--blue-lt),var(--blue))}
.blue li{color:var(--blue)}
.footer{position:absolute;left:0;top:1108px;width:920px;height:92px;background:var(--footer)}
.footer-links{position:absolute;left:46px;top:26px;font-size:10px;color:#8c8c8c}
.footer-links span{margin:0 6px}
.copyright{position:absolute;left:46px;top:48px;font-size:10px;color:#8c8c8c}
.social{position:absolute;left:723px;top:26px;display:flex;gap:6px}
.social i{width:26px;height:26px;background:#3b3b3b}
</style>
</head>
<body>
<header class="header">
  <div class="brand"><div class="brand-mark"></div><div class="brand-name">TLV ENGINEERING<br>SOLUTIONS, INC.</div></div>
  <div class="phone">Call us: 1-855-MECH-TLV</div>
  <div class="payments"><span class="label">Pay with</span>
    <div class="cards"><span>Kestrel</span><span>Norvik</span><span>Plume</span><span>Tessary</span></div>
  </div>
</header>
<nav class="nav">
  <a>Home</a><span class="sep">|</span><a>About us</a><span class="sep">|</span><a>Services</a><span class="sep">|</span><a>Solutions</a><span class="sep">|</span><a>Technologies</a><span class="sep">|</span><a>Support</a><span class="sep">|</span><a>News</a><span class="sep">|</span><a>Contact us</a>
</nav>
<section class="hero" role="img" aria-label="Photo of a robotic assembly cell with fixtures and clamps">
  <div class="hero-title">Program Robots</div>
  <div class="hero-text">Nemo enim ipsam voluptatem quia voluptas sit aspernatur aut odit aut fugit.</div>
  <div class="hero-btn">View Details</div>
  <div class="dots"><i></i><i class="on"></i><i></i></div>
</section>
<div class="shade" style="top:414px"></div>
<section class="welcome">
  <h1>Welcome to tlvengsolutions</h1>
  <p>Each situation (and company) is unique. A One-size-fits-all approach will never be the optimal solution for your business to reach its full potential. A detailed evaluation of your company's operation and a custom solution provided by TLV Engineering Solutions will take advantage of opportunities specific to your process.<br>That's what we deliver to you.</p>
  <span class="btn">Read More</span>
</section>
<div class="shade" style="top:601px"></div>
<section class="panels">
  <article class="panel red">
    <div class="panel-head">SPECIALIZING AREAS</div>
    <div class="panel-photo" role="img" aria-label="Photo of yellow industrial robots on a production line" style="background:linear-gradient(135deg,#e8c400,#b89a10 50%,#d9c23a)"></div>
    <p class="panel-text">Provide electrical and mechanical expertise to solve automation specific application problems by utilizing best known industry practices.</p>
    <ul><li>2D and 3D Capabilities</li><li>Applications</li><li>Automation Product Sales</li><li>Consulting</li><li>Onsite Startup and Engineering</li><li>Support</li><li>Contract Engineering /Techs</li><li>Panel Builds</li></ul>
    <span class="btn">View More</span>
  </article>
  <article class="panel olive">
    <div class="panel-head">EXPERTISE AREAS</div>
    <div class="panel-photo" role="img" aria-label="Photo of a robotic gripper handling a glass part" style="background:linear-gradient(135deg,#5d7c92,#9fb3c2 50%,#3e5566)"></div>
    <p class="panel-text">Provide electrical, mechanical, controls and software expertise to program, startup, debug and commission automated machinery.</p>
    <ul><li>HMI's</li><li>MOTION CONTROL</li><li>ROBOTICS</li><li>VISION</li><li>INDUSTRIAL NETWORKS</li><li>FIELDBUS</li><li>PLC's</li><li>SCADA</li></ul>
    <span class="btn">View More</span>
  </article>
  <article class="panel green">
    <div class="panel-head">PROGRAMMING LANGUAGES</div>
    <div class="panel-photo" role="img" aria-label="Photo of interlocking metal gears" style="background:linear-gradient(135deg,#6b6660,#b2a795 50%,#4d4740)"></div>
    <p class="panel-text">Design and implement control programs on PLC's, SCADA, HMI's, Vision Systems, Robots and Motion Controls specific to each application...</p>
    <ul><li>Batch</li><li>Java</li><li>C++</li><li>Javascript</li><li>IEC 61131 - 3 (PLC)</li><li>TPL / TPP</li><li>VEL+</li><li>Vista Basic</li></ul>
    <span class="btn">View More</span>
  </article>
  <article class="panel blue">
    <div class="panel-head">INDUSTRIES</div>
    <div class="panel-photo" role="img" aria-label="Photo of a robot arm on a food packaging line" style="background:linear-gradient(135deg,#cfd4d8,#8b9298 50%,#5c4038)"></div>
    <p class="panel-text">Develop controls and mechanical specifications for machines to be used when purchasing equipment. Collaborate with the systems...</p>
    <ul><li>Assembly</li><li>Distribution</li><li>Manufacturing</li><li>Material Handling</li><li>Automotive</li><li>Food and Beverage</li><li>Golf Course / Irrigation</li><li>Packaging</li></ul>
    <span class="btn">View More</span>
  </article>
</section>
<footer class="footer">
  <div class="footer-links">Home<span>/</span>About us<span>/</span>Services<span>/</span>Solutions<span>/</span>Technologies<span>/</span>Support<span>/</span>News<span>/</span>Contact us</div>
  <div class="copyright">©2015tlvengsolutions. All rights reserved.</div>
  <div class="social"><i></i><i></i><i></i><i></i><i></i></div>
</footer>
</body>
</html>
```